Brochure Design Project for a Psychotherapy Private Practice.

I am a psychologist and I own my private practice. I need brochures to market to doctors and healthcare providers so that they understand the psychotherapy services that I deliver. I also want the brochures to be informative to potential patients. I have included a word document that details the services that I offer.
Target Market(s)
Referring healthcare providers (medical doctors, naturopaths, physician assistants, nurse practitioners) and patients who are seeking psychotherapy.
Industry/Entity Type
Healthcare
Colors
Designer to choose colors to be used in the design.

```html
<!DOCTYPE html>
<html lang="en">
<head>
<meta charset="utf-8">
<title>Harbor Point Psychological Services – Brochure</title>
<link rel="stylesheet" href="https://fonts.googleapis.com/css2?family=Source+Sans+3:ital,wght@0,300;0,400;0,600;0,700;1,600&display=swap">
<style>
:root{
  --stage:#fdf0cf;
  --teal:#4a6b78;
  --teal-dark:#3e5d69;
  --teal-light:#5f7f8b;
  --ink:#222;
  --ink-soft:#444;
  --paper:#fff;
  --grey-hi:#f4f4f4;
  --grey-lo:#bdbdbd;
}
*{box-sizing:border-box;margin:0;padding:0}
html,body{width:1200px;height:1200px;overflow:hidden}
body{background:var(--stage);font-family:"Source Sans 3",sans-serif;color:var(--ink);position:relative}
.spread{position:absolute;left:46px;width:1108px;height:368px;display:flex;box-shadow:0 3px 6px rgba(0,0,0,.18)}
.spread--outside{top:189px}
.spread--inside{top:582px}
.panel{position:relative;width:369.33px;height:100%;overflow:hidden;background:var(--paper)}
.panel--scene{background:linear-gradient(180deg,var(--grey-hi) 0%,#e4e4e4 70%,var(--grey-lo) 100%)}
.art{position:absolute}
.card{position:absolute;left:20px;width:318px;background:var(--paper);border-radius:6px;box-shadow:2px 3px 5px rgba(0,0,0,.35);padding:10px 14px 0 14px}
.card h3{font-weight:600;font-size:15px;color:var(--teal);margin-bottom:4px}
.card p{font-size:9.2px;line-height:1.33;color:var(--ink)}
.tab{position:absolute;left:0;top:25px;width:170px;height:22px;background:var(--teal);border-radius:0 11px 11px 0;color:#fff;font-weight:600;font-size:14px;padding:2px 0 0 32px}
.bio-band{position:absolute;left:0;top:49px;width:100%;height:126px;background:var(--teal)}
.portrait{position:absolute;left:35px;top:11px;width:72px;height:72px;border-radius:50%;background:radial-gradient(circle at 50% 40%,#c89a7c,#6b4a35);border:3px solid #fff}
.bio-name{position:absolute;left:20px;top:86px;width:104px;text-align:center;color:#fff;font-weight:600;font-size:9.5px;line-height:1.2}
.bio-name span{display:block;font-weight:400;font-size:7.5px}
.bio-text{position:absolute;left:119px;top:16px;width:234px;color:#e6eef1;font-size:6.6px;line-height:1.44;text-align:justify}
.contact{position:absolute;left:34px;top:190px;color:var(--teal-dark)}
.contact dt{font-weight:600;font-size:12.5px;line-height:1}
.contact dd{font-weight:700;font-size:20px;line-height:1.05;margin-bottom:6px}
.address{position:absolute;left:0;width:100%;top:325px;text-align:center;font-size:7.6px;color:var(--ink-soft);line-height:1.4}
.tagline{position:absolute;left:229px;top:196px;color:var(--teal);font-weight:600;font-size:13px;line-height:1.22}
.brand{position:absolute;left:212px;top:267px;width:158px;height:60px;background:var(--paper);box-shadow:0 2px 3px rgba(0,0,0,.25);display:flex;align-items:center;gap:8px;padding-left:14px}
.brand-dot{width:20px;height:20px;border-radius:50%;background:var(--teal);flex:none}
.brand-name{font-weight:300;font-size:12.5px;line-height:1.1;color:var(--teal)}
.focus-lead{font-style:italic;font-weight:600;font-size:9.6px;line-height:1.35;margin-bottom:8px}
.areas{text-align:center}
.areas h3{color:var(--ink);font-size:14.5px;margin:4px 0 8px}
.areas ul{list-style:none;display:flex;justify-content:center;gap:22px}
.areas li{width:54px;font-size:7.6px;font-weight:600;color:var(--teal);line-height:1.3}
.areas svg{display:block;margin:0 auto 3px}
.skills-band{position:absolute;left:0;top:36px;width:100%;height:127px;background:var(--teal);color:#fff}
.skills-band h2{font-weight:600;font-size:15.5px;margin:15px 0 0 42px}
.skills-band ul{position:absolute;top:44px;list-style:disc;font-size:7.6px;line-height:1.36;color:#e6eef1}
.skills-col-a{left:74px}.skills-col-b{left:199px}
.help{position:absolute;left:0;width:100%;top:196px;text-align:center;font-size:19px;font-weight:400;line-height:1.3;color:#222}
.approach{left:16px;top:14px;width:353px;height:250px;border-radius:4px 0 0 4px}
.approach p{font-size:7.8px;line-height:1.36}
.methods{list-style:none;margin-top:10px}
.methods li{width:250px;height:19px;margin-bottom:3.4px;background:var(--teal);border-radius:9.5px;color:#fff;font-weight:600;font-size:9px;padding:3px 0 0 15px}
</style>
</head>
<body>

<section class="spread spread--outside">
  <article class="panel panel--scene">
    <div class="art" style="inset:0" role="img" aria-label="Grey background with scattered puzzle pieces"></div>
    <div class="tab">Getting Started:</div>
    <div class="card" style="top:54px;height:114px">
      <h3>Consultation</h3>
      <p>I offer a complimentary 30-minute consultation (on the phone), so you can get a sense of whether we are a good fit. It will also give me an opportunity to determine if I am the best therapist to be able to help you. In the event that we are not a good match, I can connect you with another practitioner to serve your needs.</p>
    </div>
    <div class="card" style="top:187px;height:138px">
      <h3>Intake</h3>
      <p>During our first session, we will address your presenting problem(s) and collect a thorough background of your history, so that I can best understand your problem areas in the context of who you are. We will also conduct an assessment of your current symptoms, address provisional diagnoses (if applicable), discuss potential treatment goals, and develop a tentative treatment plan with recommendations for therapy duration and frequency.</p>
    </div>
  </article>

  <article class="panel">
    <div class="bio-band">
      <div class="portrait" role="img" aria-label="Portrait photo of the psychologist"></div>
      <p class="bio-name">Elena Varkas<span>Psychologist, PsyD</span></p>
      <p class="bio-text">Dr. Varkas graduated from Westbrook University and received her Doctoral degree in Clinical Psychology at the Bayview School of Professional Psychology. She completed her predoctoral internship in behavioral medicine and rehabilitation psychology at the Northshore Veterans Health Center/Eastfield Medical School and a postdoctoral fellowship at the Cognitive Intensive Outpatient Program, Mesa Ridge Hospital, Lakeport. Dr. Varkas is a member of the National Psychological Society, Guild of Cognitive Therapy, and the Coastal County Psychological Association.</p>
    </div>
    <dl class="contact">
      <dt>For Appointments</dt><dd>000 000 0000</dd>
      <dt>Mail Us</dt><dd>info@harborpointpsych.com</dd>
      <dt>Website</dt><dd>www.harborpointpsych.com</dd>
    </dl>
    <p class="address">Address: Lorem ipsum dolor sit amet, consectetuer,<br>adipiscing elit, sed diam nonummy, euismod</p>
  </article>

  <article class="panel panel--scene">
    <div class="art" style="left:20px;top:10px;width:200px;height:340px;background:radial-gradient(ellipse at 45% 50%,#3f5f6c 0%,#6d8f9c 45%,rgba(230,230,230,0) 72%)" role="img" aria-label="Illustration of a human head built from teal puzzle pieces"></div>
    <p class="tagline">a<br>practical<br>approach<br>to problem-solving</p>
    <div class="brand"><span class="brand-dot"></span><span class="brand-name">Harbor Point<br>Psychological<br>Services</span></div>
  </article>
</section>

<section class="spread spread--inside">
  <article class="panel panel--scene">
    <div class="art" style="inset:0" role="img" aria-label="Grey background with scattered puzzle pieces"></div>
    <div class="card" style="top:8px;height:167px;padding-top:22px">
      <h3>Treatment Focus</h3>
      <p class="focus-lead">I pride myself on being more than just someone to listen, but someone who takes a hands-on, practical approach to problem-solving.</p>
      <p style="font-size:8px">It's important to face the challenges of life head-on, but with the right skills and tools in your toolbox. I aim to build a collaborative relationship with you and assist you in understanding the relationship between negative thought patterns and ineffective coping strategies. We work together to develop a healthier thought process and effective coping skills, ultimately decreasing symptoms and improving your overall quality of life.</p>
    </div>
    <div class="card areas" style="top:188px;height:138px">
      <h3>My Areas of Focus Include:</h3>
      <ul>
        <li><svg width="42" height="42" viewBox="0 0 42 42"><circle cx="21" cy="21" r="20" fill="#4a6b78"/><circle cx="21" cy="21" r="15" fill="none" stroke="#fff" stroke-width="1.5"/></svg>Adult Therapy</li>
        <li><svg width="42" height="42" viewBox="0 0 42 42"><circle cx="21" cy="21" r="20" fill="#4a6b78"/><circle cx="21" cy="21" r="15" fill="none" stroke="#fff" stroke-width="1.5"/></svg>Adolescent Therapy</li>
        <li><svg width="42" height="42" viewBox="0 0 42 42"><circle cx="21" cy="21" r="20" fill="#4a6b78"/><circle cx="17" cy="22" r="7" fill="none" stroke="#fff" stroke-width="2.2"/><circle cx="25" cy="22" r="7" fill="none" stroke="#fff" stroke-width="2.2"/></svg>Couples Therapy</li>
      </ul>
    </div>
  </article>

  <article class="panel">
    <div class="skills-band">
      <svg class="art" style="left:0;top:0" width="370" height="127" aria-hidden="true"><polygon points="0,55 80,25 370,55 370,110 0,110" fill="#5a7a86" opacity=".45"/></svg>
      <h2 style="position:relative">Typical Skills Developed in Treatment:</h2>
      <ul class="skills-col-a">
        <li>Assertive Communication</li><li>Cognitive Restructuring</li><li>Decatastrophizing</li><li>Distress Tolerance</li><li>Emotion Regulation</li><li>Healthy Grieving of Losses</li>
      </ul>
      <ul class="skills-col-b">
        <li>Healthy Personal Boundaries</li><li>Interpersonal Effectiveness</li><li>Imagery Techniques</li><li>Mindfulness</li><li>Problem Solving</li><li>Stress Management</li>
      </ul>
    </div>
    <p class="help">I need your help to fill up this<br>space</p>
  </article>

  <article class="panel panel--scene">
    <div class="art" style="left:40px;top:240px;width:200px;height:128px;background:radial-gradient(ellipse at 50% 40%,#2e2e2e,rgba(200,200,200,0) 70%)" role="img" aria-label="Base of a head illustration made of dark puzzle pieces"></div>
    <div class="card approach">
      <h3 style="color:var(--teal);margin-top:4px">My Approach:</h3>
      <p>As a clinical psychologist, I deliver a treatment approach that is genuine, direct, and effective. My treatment approach is tailored to each client and typically involves a blend of evidenced based treatments including Cognitive Behavioral Therapy, Dialectical Behavior Therapy, Imagery Rehearsal Therapy, Interpersonal Psychotherapy, and Mindfulness-Based Stress Reduction. Together we'll work to uncover and better understand life's challenges and day-to-day stressors that detract from your life and focus, and begin identifying and practicing things that will improve your overall quality of life.</p>
      <ul class="methods">
        <li>Cognitive Behavioral Therapy (CBT)</li>
        <li>Dialectical Behavior Therapy (DBT)</li>
        <li>Imagery Rehearsal Therapy (IRT)</li>
        <li>Interpersonal Psychotherapy (IPT)</li>
        <li>Mindfulness-Based Stress Reduction (MBSR)</li>
      </ul>
    </div>
  </article>
</section>

</body>
</html>
```